Long Term Insurance for Maturing Women

My business, is a Full service Life and Property Insurance Agency.. I want a reply card, Gloss, with woman showing Maturity, on a beach looking out at a Sun Set, with light Colors of Rainbow.
Thinking: If I am alone, how much income will I need to pay for a Long Term Sickness or Injury. ?
Do I have enough money set aside to cover the added expenses of a long Term Illness ?
Have I enough Life Insurance to cover final expenses, and leave my love ones free of any Debt from my Passing ?
These are real life's concerns, Please Call, let's start finding answers today !
Mark Doverby, Agent # 0718243 at (555-203-4817) - Halvert Insurance & Financial Service LLC.
Markdov@halvertins.example 4100 Birchwell Rd, Cypress Ca. 90000

Industry/Entity Type

Business

```html
<!DOCTYPE html>
<html lang="en">
<head>
<meta charset="utf-8">
<title>Reply Card – Halvert Insurance &amp; Financial Service LLC</title>
<link rel="stylesheet" href="https://fonts.googleapis.com/css2?family=Noto+Sans:wght@400;700&family=Tinos:wght@400&family=Ubuntu:wght@300;400&display=swap">
<style>
  :root {
    --page-bg: #e6e8ea;
    --sky-deep: #1b5fd6;
    --sky-mid: #3f94ee;
    --sea: #5fd3da;
    --surf: #d8f4ef;
    --sand: #e9eec8;
    --sand-pale: #f4f5e6;
    --question-white: #ffffff;
    --band-line: rgba(255, 255, 255, 0.55);
    --navy: #1a3a8a;
    --teal: #3a97a8;
    --ink: #111111;
    --message-blue: #2c6fd4;
    --card-white: #ffffff;
    --stamp-line: #222222;
  }
  * { margin: 0; padding: 0; box-sizing: border-box; }
  html, body { width: 1200px; height: 1000px; overflow: hidden; }
  body { background: var(--page-bg); position: relative; }

  .card {
    position: absolute;
    width: 660px;
    height: 460px;
    overflow: hidden;
    background: var(--card-white);
    box-shadow: 0 6px 18px rgba(0, 0, 0, 0.18);
  }
  .card--front { left: 30px; top: 30px; }
  .card--back { left: 510px; top: 510px; }

  /* Front */
  .front__scene {
    position: absolute; inset: 0;
    background: linear-gradient(180deg,
      var(--sky-deep) 0%, var(--sky-mid) 28%, #8fd0f2 44%,
      var(--sea) 52%, var(--surf) 62%, var(--sand) 75%, var(--sand-pale) 100%);
  }
  .front__portrait {
    position: absolute;
    left: 455px; top: 225px; width: 150px; height: 235px;
    background: linear-gradient(180deg, #7a4a3a 0%, #c99a86 22%, #f2ede6 40%, #ffffff 100%);
    border-radius: 60px 60px 6px 6px;
    opacity: 0.92;
  }
  .questions {
    position: absolute; left: 150px; top: 62px; width: 470px;
    font-family: "Noto Sans", Verdana, sans-serif;
    color: var(--question-white);
    font-size: 13.5px; line-height: 1.28;
    text-align: center;
    text-shadow: 0 1px 2px rgba(0, 40, 120, 0.35);
  }
  .questions__item { padding: 6px 0 8px; border-bottom: 1.5px solid var(--band-line); }
  .questions__item:last-child { border-bottom: none; }

  .call-to-action {
    position: absolute; left: 60px; top: 330px; width: 380px;
    font-family: "Tinos", "Times New Roman", serif;
    color: var(--navy); font-size: 17px; line-height: 1.2;
    text-align: center;
  }
  .agent {
    position: absolute; left: 62px; top: 382px;
    font-family: "Ubuntu", Arial, sans-serif; font-weight: 300;
    color: var(--teal); font-size: 14.5px; line-height: 1.25;
  }
  .agent__firm { white-space: nowrap; }
  .contact {
    position: absolute; left: 62px; top: 488px;
    font-family: "Noto Sans", Verdana, sans-serif; font-weight: 700;
    color: var(--ink); font-size: 11px; line-height: 1.3;
  }
  .card--front .contact { top: auto; bottom: 12px; }
  .card--front .agent { top: 350px; left: 40px; }
  .card--front .call-to-action { top: 280px; }

  /* Back */
  .back__scene {
    position: absolute; left: 0; top: 0; width: 380px; height: 460px;
    background: linear-gradient(180deg,
      var(--sky-deep) 0%, var(--sky-mid) 16%, #9fd7f3 26%,
      var(--sea) 30%, var(--surf) 38%, var(--sand) 55%, var(--sand-pale) 100%);
  }
  .back__message {
    position: absolute; left: 55px; top: 125px; width: 230px; height: 100px;
  }
  .back__message-text {
    position: absolute; inset: 0;
    display: flex; align-items: center; justify-content: center;
    text-align: center;
    font-family: "Noto Sans", Verdana, sans-serif;
    color: var(--message-blue); font-size: 15px; line-height: 1.2;
  }
  .stamp-box {
    position: absolute; right: 48px; top: 32px;
    width: 110px; height: 125px;
    border: 2px solid var(--stamp-line);
  }
</style>
</head>
<body>

  <section class="card card--front" aria-label="Reply card front">
    <div class="front__scene" role="img" aria-label="Photo of a bright tropical beach with blue sky, turquoise sea, a small island and a soft rainbow"></div>
    <div class="front__portrait" role="img" aria-label="Photo of a mature woman in white sitting on the sand, gazing thoughtfully upward"></div>

    <div class="questions">
      <p class="questions__item">If I am alone, how much income will I need to pay for a Long Term Sickness or Injury. ?</p>
      <p class="questions__item">Do I have enough money set aside to cover the added expenses of a long Term Illness ?</p>
      <p class="questions__item">Have I enough Life Insurance to cover final expenses, and leave my love ones free of any Debt from my Passing ?</p>
    </div>

    <p class="call-to-action">These are real life's concerns,<br>Please Call, let's start finding answers today !</p>

    <div class="agent">
      <p>Mark Doverby,</p>
      <p>Agent # 0718243</p>
      <p>at (555-203-4817) -</p>
      <p class="agent__firm">Halvert Insurance &amp; Financial Service LLC.</p>
    </div>

    <div class="contact">
      <p>Markdov@halvertins.example</p>
      <p>4100 Birchwell Rd, Cypress Ca. 90000</p>
    </div>
  </section>

  <section class="card card--back" aria-label="Reply card back">
    <div class="back__scene" role="img" aria-label="Photo of a tropical beach with a small green island on the horizon and a soft shadow on the sand"></div>
    <div class="back__message">
      <svg width="230" height="100" viewBox="0 0 230 100" aria-hidden="true">
        <ellipse cx="115" cy="50" rx="112" ry="47" fill="rgba(255,255,255,0.45)" stroke="rgba(255,255,255,0.9)" stroke-width="3"/>
      </svg>
      <p class="back__message-text">Are you ready for<br>tomorrow?</p>
    </div>
    <div class="stamp-box" aria-label="Stamp area"></div>
  </section>

</body>
</html>
```